Friendly, Professional, Simple Catering Menu

Currently we cater but don't have a take-out menu for customers to order from or see our options and we want to change that. Most of the customers we cater are employees of large and small businesses, we also have some private parties we cater to as well. With this in mind we are looking for a professional looking menu but also to have some personal touch with it. The format should be easy to read and understand. We are looking to hand out this menu to local businesses, schools and offices, and maybe after a few trial runs, our store too. Locally, we have a pretty established name but our options can't be seen by the public and we are looking to make that possible with this catering menu. Originally we were thinking of tri-fold menu, 8.5inx14in, but after seeing some of the work done already we trust the designers to create something they think would be the right fit. We don't want it too large nor too small to ensure it won't be an inconvenience for businesses, it must still stand out enough to grab their attention.
Target Market(s)
Businesses, Schools, Office buildings, and Private parties.
Industry/Entity Type
Catering

```html
<!DOCTYPE html>
<html lang="en">
<head>
<meta charset="utf-8">
<title>Kettle &amp; Crumb Catering Menu</title>
<link href="https://fonts.googleapis.com/css2?family=Roboto+Slab:wght@400;700;800&family=Montserrat:wght@600;700&family=Oswald:wght@600&display=swap" rel="stylesheet">
<style>
:root{
  --cream:#fbf0cd;
  --red:#e31e24;
  --ink:#231f20;
  --white:#ffffff;
}
*{box-sizing:border-box;margin:0;padding:0}
html,body{width:1200px;height:729px;overflow:hidden;background:var(--cream)}
.menu{position:relative;width:1200px;height:729px;overflow:hidden;background:var(--cream);font-family:"Roboto Slab",serif;color:var(--ink)}
.abs{position:absolute}
.brand-mini{position:absolute;width:60px;font-family:"Roboto Slab",serif;font-weight:800;color:var(--red);font-size:11px;line-height:12px;text-align:center;text-transform:uppercase}
.section-title{position:absolute;font-family:"Roboto Slab",serif;font-weight:700;color:var(--red);font-size:24px;line-height:26px}
.note{position:absolute;font-style:italic;font-size:7.5px;line-height:11px;font-weight:700}
.item{position:absolute}
.item-name{font-weight:700;color:var(--red);font-size:18px;line-height:20px}
.item-price{font-weight:700;font-size:10.5px;line-height:14px}
.item-price em{color:var(--red);font-weight:400;font-size:7.5px;margin-left:4px}
.item-price .or{color:var(--red);font-family:"Montserrat",sans-serif;font-size:7.5px;margin:0 8px}
.trays{position:absolute;left:30px;top:238px;display:flex;gap:14px}
.tray{display:flex;align-items:center;gap:4px}
.tray-badge{width:20px;height:20px;border-radius:50%;background:var(--red);color:var(--white);font-size:8px;font-weight:700;display:flex;align-items:center;justify-content:center}
.tray-label{font-family:"Montserrat",sans-serif;color:var(--red);font-size:6.5px;line-height:7px}
.tray-price{font-weight:700;font-size:11px;line-height:11px}
.photo{position:absolute;overflow:hidden}
.photo-caption{position:absolute;color:var(--white);font-weight:700;font-size:17px;line-height:20px;white-space:nowrap}
.rule{position:absolute;height:1px;background:var(--red)}
.welcome{position:absolute;left:40px;top:408px;width:354px;text-align:center;font-size:9.5px;line-height:13.5px}
.cta{position:absolute;left:40px;top:461px;width:354px;text-align:center;font-family:"Montserrat",sans-serif;font-weight:700;color:var(--red);font-size:7.8px;letter-spacing:.2px}
.loc-name{font-family:"Montserrat",sans-serif;font-weight:700;color:var(--red);font-size:10px;line-height:12px;letter-spacing:.3px}
.loc-detail{font-style:italic;font-size:7.5px;line-height:9.4px}
.contact{position:absolute;left:30px;top:604px;font-size:7.5px;line-height:13px}
.contact b{display:inline-block;width:65px;font-family:"Montserrat",sans-serif;color:var(--red);font-size:10px;letter-spacing:.3px}
.contact i{font-size:7.5px}
.ask-lead{position:absolute;left:109px;top:658px;font-family:"Montserrat",sans-serif;font-weight:600;font-size:9.6px;letter-spacing:.3px}
.ask{position:absolute;left:106px;top:671px;font-weight:700;color:var(--red);font-size:20.5px;line-height:24px;white-space:nowrap}
.cover-mark{position:absolute;left:1022px;top:408px;width:140px;height:140px;border-radius:50%;background:var(--ink)}
.cover-name{position:absolute;right:28px;top:552px;text-align:right;font-family:"Oswald",sans-serif;font-weight:600;color:var(--red);font-size:52px;line-height:58px;text-transform:uppercase;white-space:nowrap}
.cover-name span{display:block}
.cover-sub{position:absolute;right:30px;top:674px;text-align:right;font-family:"Roboto Slab",serif;font-weight:700;font-style:italic;color:var(--red);font-size:14px;line-height:18px;white-space:nowrap}
</style>
</head>
<body>
<main class="menu">

  <div class="brand-mini" style="left:28px;top:28px">Kettle &amp; Crumb</div>
  <h2 class="section-title" style="left:97px;top:23px">Desserts</h2>
  <p class="note" style="left:97px;top:50px">Desserts will be supplied by, *Sugar Lane Bakery.<br>Menu options:</p>

  <div class="item" style="left:30px;top:86px"><div class="item-name">Cookies</div><div class="item-price">$0.75<em>each</em></div></div>
  <div class="item" style="left:228px;top:86px"><div class="item-name">Brownie</div><div class="item-price">$1.25<em>each</em></div></div>
  <div class="item" style="left:30px;top:127px"><div class="item-name">Blondie</div><div class="item-price">$1.25<em>each</em></div></div>
  <div class="item" style="left:228px;top:127px"><div class="item-name">Pumpkin bar</div><div class="item-price">$1.25<em>each</em></div></div>
  <div class="item" style="left:30px;top:169px"><div class="item-name">Cake Pops</div><div class="item-price">$15<em>per dozen</em></div></div>
  <div class="item" style="left:228px;top:169px"><div class="item-name">Cupcakes</div><div class="item-price">$3.25<em>each</em><span class="or">OR</span>$30<em>per dozen</em></div></div>
  <div class="item" style="left:30px;top:213px"><div class="item-name">Cake Pops</div></div>

  <div class="trays">
    <div class="tray"><span class="tray-badge">1/4</span><span><div class="tray-label">TRAY</div><div class="tray-price">$25</div></span></div>
    <div class="tray"><span class="tray-badge">1/2</span><span><div class="tray-label">TRAY</div><div class="tray-price">$45</div></span></div>
    <div class="tray"><span class="tray-badge">Full</span><span><div class="tray-label">TRAY</div><div class="tray-price">$85</div></span></div>
  </div>

  <div class="photo" role="img" aria-label="Three frosted cupcakes: red velvet, chocolate and caramel" style="left:30px;top:285px;width:178px;height:85px;border-radius:8px;background:linear-gradient(180deg,#f6ead8 0%,#c98a6a 55%,#8e1e22 100%)"></div>
  <div class="photo" role="img" aria-label="Sundae cups with cherries, brownies and chocolate chip cookies" style="left:224px;top:218px;width:172px;height:152px;border-radius:8px;background:linear-gradient(180deg,#f2ede4 0%,#a8805c 55%,#5a3722 100%)"></div>

  <div class="rule" style="left:35px;top:390px;width:363px"></div>
  <p class="welcome">All of us here at Kettle &amp; Crumb sincerely hope that your visit is a pleasurable one. Please don't hesitate to notify us if there is anything that we can do to make your experience more enjoyable. Thanks so much!</p>
  <p class="cta">CHECK OUT OUR CATERING MENU FOR YOUR NEXT PARTY OR EVENT.</p>
  <div class="rule" style="left:30px;top:490px;width:373px"></div>

  <svg class="abs" style="left:28px;top:504px" width="34" height="34" viewBox="0 0 34 34" aria-hidden="true">
    <circle cx="17" cy="17" r="15" fill="none" stroke="#e31e24" stroke-width="1.6"/>
    <path d="M17 8a6 6 0 0 0-6 6c0 5 6 11 6 11s6-6 6-11a6 6 0 0 0-6-6z" fill="#231f20"/>
    <circle cx="17" cy="14" r="2.2" fill="#fbf0cd"/>
  </svg>
  <h2 class="section-title" style="left:73px;top:507px;font-size:19px">Locations/Info</h2>

  <div class="abs" style="left:30px;top:547px">
    <div class="loc-name">WESTGATE COMMONS</div>
    <div class="loc-detail">1040 Westgate Commons<br>Mon–Sat: 10:30am–9pm<br>Sun: 11am–7pm<br>(555)-201-4410</div>
  </div>
  <div class="abs" style="left:228px;top:547px">
    <div class="loc-name">DOWNTOWN RIVERTON</div>
    <div class="loc-detail">2210 4th Avenue North<br>Mon–Sat: 10:30am–3pm<br>Sun: Closed<br>(555)-207-3382</div>
  </div>
  <div class="contact">
    <div><b>EMAIL:</b><i>hello@kettleandcrumb.com</i></div>
    <div><b>WEBSITE:</b><i>www.kettleandcrumb.com</i></div>
  </div>

  <div class="rule" style="left:30px;top:643px;width:373px"></div>
  <div class="brand-mini" style="left:33px;top:663px">Kettle &amp; Crumb</div>
  <p class="ask-lead">HOW 'BOUT SOME SOUP AND SALAD?</p>
  <p class="ask">Ask about Kettle &amp; Crumb</p>
  <div class="rule" style="left:30px;top:705px;width:373px"></div>

  <div class="brand-mini" style="left:416px;top:28px">Kettle &amp; Crumb</div>
  <h2 class="section-title" style="left:486px;top:23px">Our products<br>we supply!</h2>

  <div class="photo" role="img" aria-label="Garden salad with lettuce, cheddar, cucumber slices and cherry tomatoes" style="left:418px;top:87px;width:373px;height:147px;background:linear-gradient(100deg,#c9c9a8 0%,#e9b340 35%,#d8e2b4 55%,#c42a1c 75%,#a6c45a 100%)">
    <span class="photo-caption" style="right:14px;bottom:6px">Garden Salads</span>
  </div>
  <div class="photo" role="img" aria-label="Caesar salad bowl with croutons, chicken, parmesan and bacon" style="left:418px;top:244px;width:373px;height:147px;background:linear-gradient(90deg,#2a2a2a 0%,#c98a32 25%,#9c8a78 45%,#eadcb0 60%,#8a3a22 75%,#c98a32 90%,#2a2a2a 100%)">
    <span class="photo-caption" style="left:30px;bottom:12px;transform:rotate(-90deg);transform-origin:left bottom">Caesar Salad</span>
  </div>
  <div class="photo" role="img" aria-label="Bowls of soups and sides with serving tongs on a buffet table" style="left:418px;top:401px;width:373px;height:147px;background:linear-gradient(120deg,#6b5138 0%,#d6c7a0 40%,#3a3a3a 60%,#e8962a 85%,#5a4532 100%)">
    <span class="photo-caption" style="left:8px;top:8px">Famous Five Soups</span>
  </div>
  <div class="photo" role="img" aria-label="Platter of sliced deli sandwiches on white and wheat bread" style="left:418px;top:558px;width:373px;height:147px;background:linear-gradient(100deg,#3a2a22 0%,#9a6a44 25%,#efe2c8 50%,#d9a890 70%,#b0262a 100%)">
    <span class="photo-caption" style="right:16px;bottom:8px">Sandwiches</span>
  </div>

  <div class="cover-mark" aria-hidden="true"></div>
  <h1 class="cover-name"><span>Kettle</span><span>&amp;&#8202;Crumb</span></h1>
  <p class="cover-sub">Catering Menu</p>

</main>
</body>
</html>
```